Cool modern, tech Business card design

Looking for a new business card design for our Managed IT Services company. We would like 2 sides, with the logo one one side horizontally and then the information on the back in either vertical or horizontal. We want our colors from the logo incorporated but also would like to see the color gray in there as well.

Target Market(s)

IT, Information Technology, Tech, Service

Industry/Entity Type

It Service

Contact Information for Business Card

Carl Penner
Managing Partner
(P)555-271-4830 ext xxx
(F)555-271-4831
www.brixtelcore.com

Font styles to use
Sans Serif

Colors
959595
000000
ec1f27

Requirements
Must have
• Logo on one side with some nice design or pattern
• Information on back in either vertical or horizontal format
Nice to have
• For it to look cool, tech, modern, stand out.

```html
<!DOCTYPE html>
<html lang="en">
<head>
<meta charset="utf-8">
<title>Brixtelcore Business Card</title>
<link href="https://fonts.googleapis.com/css2?family=Alegreya+Sans:wght@500;700&display=swap" rel="stylesheet">
<style>
  :root {
    --brand-red: #cc1530;
    --brand-charcoal: #231f20;
    --brand-white: #ffffff;
    --stage: #1c1c1c;
  }
  * { margin: 0; padding: 0; box-sizing: border-box; }
  html, body {
    width: 1125px;
    height: 1200px;
    overflow: hidden;
    background: var(--stage);
    font-family: "Alegreya Sans", sans-serif;
  }
  .card {
    position: absolute;
    left: 171px;
    width: 826px;
    height: 470px;
    overflow: hidden;
  }
  .card--front { top: 106px; background: var(--brand-charcoal); }
  .card--back { top: 659px; background: var(--brand-white); }

  .front-panel {
    position: absolute;
    left: 0;
    top: 0;
    width: 420px;
    height: 100%;
    background: var(--brand-red);
  }
  .front-artwork {
    position: absolute;
    left: 420px;
    top: 0;
    width: 270px;
    height: 100%;
    background: linear-gradient(90deg, var(--brand-red) 0%, #a5182a 55%, var(--brand-charcoal) 100%);
  }

  .holder {
    position: absolute;
    left: 50px;
    top: 106px;
    color: var(--brand-white);
    text-transform: uppercase;
  }
  .holder__name { font-weight: 700; font-size: 31px; line-height: 1; letter-spacing: 0.5px; }
  .holder__title { font-weight: 700; font-size: 21px; line-height: 1; margin-top: 6px; letter-spacing: 0.4px; }

  .company-name {
    position: absolute;
    left: 48px;
    top: 196px;
    color: var(--brand-white);
    font-weight: 700;
    font-size: 58px;
    line-height: 1;
    letter-spacing: -0.5px;
  }

  .contact-list {
    position: absolute;
    left: 50px;
    top: 283px;
    list-style: none;
    color: var(--brand-white);
    font-weight: 700;
    font-size: 22px;
    line-height: 27px;
  }
  .contact-list li { display: flex; align-items: center; gap: 12px; }
  .contact-list svg { width: 19px; height: 19px; fill: var(--brand-white); flex: none; }

  .back-brand {
    position: absolute;
    left: 0;
    right: 0;
    top: 232px;
    display: flex;
    justify-content: center;
    align-items: center;
    gap: 16px;
  }
  .back-brand__name {
    color: var(--brand-charcoal);
    font-weight: 700;
    font-size: 72px;
    line-height: 1;
    letter-spacing: -0.5px;
  }
  .back-brand__mark {
    width: 30px;
    height: 30px;
    background: var(--brand-red);
  }
</style>
</head>
<body>

<section class="card card--front">
  <div class="front-panel"></div>
  <div class="front-artwork" role="img" aria-label="Decorative red and white chevron swoosh"></div>

  <div class="holder">
    <p class="holder__name">Carl Penner</p>
    <p class="holder__title">Managing Partner</p>
  </div>

  <p class="company-name">brixtelcore</p>

  <ul class="contact-list">
    <li>
      <svg viewBox="0 0 20 20" aria-hidden="true"><path d="M2 7 C2 4 6 3 10 3 C14 3 18 4 18 7 V8 H14 V6.5 H6 V8 H2 Z M5 9 H15 L17 16 H3 Z M10 10.5 A2.5 2.5 0 1 0 10 15.5 A2.5 2.5 0 1 0 10 10.5 Z"/></svg>
      <span>555-271-4830 ext 254</span>
    </li>
    <li>
      <svg viewBox="0 0 20 20" aria-hidden="true"><path d="M5 2 H15 V7 H5 Z M2 8 H18 V15 H15 V12 H5 V15 H2 Z M6 13 H14 V18 H6 Z"/></svg>
      <span>555-271-4831</span>
    </li>
    <li>
      <svg viewBox="0 0 20 20" aria-hidden="true"><path d="M10 2 A8 8 0 1 0 10 18 A8 8 0 1 0 10 2 Z M6 6 C8 5 9 7 8 9 C7 10 9 12 8 14 C6 13 5 10 6 6 Z M12 5 C14 6 15 8 14 10 C12 10 11 8 12 5 Z"/></svg>
      <span>www.brixtelcore.com</span>
    </li>
  </ul>
</section>

<section class="card card--back">
  <div class="back-brand">
    <span class="back-brand__name">brixtelcore</span>
    <span class="back-brand__mark" aria-hidden="true"></span>
  </div>
</section>

</body>
</html>
```